Tallgrove Vale Management

I need a professional website. My current website is tallgrovevalemanagement.com and I hate it. It was created with some AI tool very quickly because I needed a site up and running with no advanced notice. I’m open to all designs .. I trust you, the professionals will deliver the results I’m anxiously awaiting! :)

```html
<!DOCTYPE html>
<html lang="en">
<head>
<meta charset="utf-8">
<title>About Us – Tallgrove Vale Management</title>
<link rel="stylesheet" href="https://fonts.googleapis.com/css2?family=Figtree:wght@400;500;600;700;800&display=swap">
<style>
:root{
  --navy:#1b2a57;
  --navy-deep:#14204a;
  --red:#c8202b;
  --ink:#1f2433;
  --text:#2c3140;
  --muted:#5b6170;
  --light:#f2f3f5;
  --white:#ffffff;
  --rule:#d9dce3;
}
*{margin:0;padding:0;box-sizing:border-box}
html,body{width:1200px;height:2219px;overflow:hidden}
body{font-family:"Figtree",Arial,sans-serif;color:var(--text);background:var(--white);position:relative}
.abs{position:absolute}
.eyebrow{font-size:11px;font-weight:700;color:var(--red);letter-spacing:.04em;display:flex;align-items:center;gap:12px}
.eyebrow::after{content:"";width:46px;height:1px;background:#9aa0ad}
.h2{font-weight:800;color:var(--navy);font-size:30px;line-height:1.2}
.dot{color:var(--red)}

/* hero */
.hero{position:absolute;left:0;top:0;width:1200px;height:425px;overflow:hidden}
.hero-photo{position:absolute;inset:0;background:linear-gradient(100deg,#3a4560 0%,#5b6377 35%,#7c7f86 60%,#4d5468 100%)}
.hero-shade{position:absolute;inset:0;background:linear-gradient(90deg,rgba(20,32,74,.75),rgba(20,32,74,.35) 60%,rgba(20,32,74,.2))}
.hero-panel{position:absolute;inset:0;background:var(--navy);clip-path:polygon(794px 72px,1200px 72px,1200px 425px,599px 425px)}
.hero-edge{position:absolute;inset:0}
.nav{position:absolute;left:0;top:0;width:1200px;height:80px;background:rgba(20,32,74,.55);border-bottom:1px solid rgba(255,255,255,.15)}
.brand{position:absolute;left:40px;top:20px;display:flex;align-items:center;gap:8px;font-weight:800;font-size:15px;line-height:1.1;color:var(--white)}
.brand .sq{width:14px;height:14px;background:var(--red)}
.menu{position:absolute;top:34px;left:0;list-style:none}
.menu li{position:absolute;white-space:nowrap;font-size:11px;font-weight:700;color:var(--white);text-transform:uppercase}
.menu li.active::after{content:"";position:absolute;left:0;right:0;top:30px;height:3px;background:var(--red)}
.phone-box{position:absolute;left:966px;top:0;width:234px;height:80px;background:var(--red);display:flex;align-items:center;justify-content:center;gap:10px;color:var(--white);font-weight:700;font-size:17px}
.hero-title{position:absolute;left:154px;top:160px;font-size:42px;font-weight:700;color:var(--white)}
.hero-rule{position:absolute;left:154px;top:219px;width:120px;height:3px;background:var(--red)}
.hero-sub{position:absolute;left:154px;top:263px;font-size:22px;line-height:31px;color:var(--white)}
.hero-name{position:absolute;left:770px;top:205px;width:300px;text-align:center;color:var(--white);font-weight:800;font-size:38px;line-height:1.05;text-transform:uppercase}

/* who */
.who-copy{position:absolute;left:141px;top:486px;width:390px}
.who-copy .h2{margin-top:24px}
.who-copy p{font-size:13px;line-height:23.4px;color:var(--text);margin-top:18px}
.btn-red{display:inline-flex;align-items:center;gap:12px;background:var(--red);color:var(--white);font-size:11px;font-weight:700;text-transform:uppercase;padding:0 22px;height:38px}
.who-copy .btn-red{margin-top:24px}
.office{position:absolute;left:609px;top:485px;width:451px;height:413px;background:linear-gradient(90deg,#3e4146 0%,#55585e 55%,#8d96a3 75%,#c7ced8 100%)}

/* values */
.values-head{position:absolute;left:0;top:953px;width:1200px;text-align:center}
.values-head .eyebrow{justify-content:center}
.values-head .h2{font-size:29px;margin-top:16px}
.values-head .bar{width:30px;height:3px;background:var(--red);margin:14px auto 0}
.value{position:absolute;top:1055px;width:180px;text-align:center}
.value svg{display:block;margin:0 auto}
.value h3{margin-top:26px;font-size:15px;font-weight:800;color:var(--navy);text-transform:uppercase}
.value p{margin-top:10px;font-size:12px;line-height:18px;color:var(--text)}
.vdiv{position:absolute;top:1058px;width:1px;height:155px;background:var(--rule)}

/* team */
.team{position:absolute;left:0;top:1261px;width:1200px;height:320px;background:var(--light);overflow:hidden}
.team-copy{position:absolute;left:111px;top:50px;width:400px}
.team-copy .h2{margin-top:16px}
.team-copy p{margin-top:18px;font-size:13px;line-height:21.5px}
.btn-outline{margin-top:24px;display:inline-flex;align-items:center;gap:12px;border:1.5px solid var(--red);color:var(--navy);font-size:11px;font-weight:700;text-transform:uppercase;padding:0 18px;height:36px;background:var(--white)}
.team-photo{position:absolute;inset:0}

/* stats */
.stats{position:absolute;left:0;top:1581px;width:1200px;height:190px;background:var(--navy)}
.stat{position:absolute;top:30px;width:240px;text-align:center;color:var(--white)}
.stat svg{display:block;margin:0 auto}
.stat .bar{width:38px;height:3px;background:var(--red);margin:10px auto 0}
.stat strong{display:block;font-size:30px;font-weight:800;margin-top:10px}
.stat span{display:block;font-size:14px;margin-top:6px}
.sdiv{position:absolute;top:33px;width:1px;height:125px;background:rgba(255,255,255,.22)}

/* cta */
.cta{position:absolute;left:0;top:1771px;width:1200px;height:167px;background:linear-gradient(90deg,#2a3560 0%,#3a4568 55%,#4c5573 100%)}
.cta-bar{position:absolute;left:111px;top:47px;width:4px;height:95px;background:var(--red)}
.cta h2{position:absolute;left:133px;top:44px;font-size:29px;font-weight:800;color:var(--white)}
.cta p{position:absolute;left:133px;top:96px;width:460px;font-size:14px;line-height:21px;color:#e6e8ef}
.cta .btn-red{position:absolute;left:800px;top:64px;height:46px;padding:0 28px;font-size:13px}

/* footer */
.footer{position:absolute;left:0;top:1938px;width:1200px;height:281px;background:var(--navy-deep);color:var(--white)}
.f-brand{position:absolute;left:102px;top:40px;display:flex;align-items:center;gap:8px;font-weight:800;font-size:18px;line-height:1.1}
.f-brand .sq{width:16px;height:16px;background:var(--red)}
.f-blurb{position:absolute;left:102px;top:150px;width:220px;font-size:11.5px;line-height:17px;color:#dfe2ea}
.f-social{position:absolute;left:102px;top:215px;display:flex;gap:7px}
.f-social i{display:block;width:22px;height:22px;border-radius:50%;background:var(--white)}
.f-col{position:absolute;top:35px}
.f-col h4{font-size:12.5px;font-weight:700;text-transform:uppercase;margin-bottom:14px}
.f-col ul{list-style:none}
.f-col li{font-size:11.5px;line-height:23.4px;color:#dfe2ea}
.f-contact li{display:flex;gap:12px;align-items:flex-start;line-height:17px;margin-bottom:14px}
.f-contact svg{flex:none;margin-top:1px}
.f-bottom{position:absolute;left:102px;right:102px;top:249px;border-top:1px solid rgba(255,255,255,.15)}
.f-copy{position:absolute;left:102px;top:258px;font-size:10px;color:#a9afc0}
.f-legal{position:absolute;left:867px;top:258px;font-size:10px;color:#dfe2ea;display:flex;gap:14px}
</style>
</head>
<body>

<header class="hero">
  <div class="hero-photo" role="img" aria-label="Row of residential houses along a tree-lined street"></div>
  <div class="hero-shade"></div>
  <div class="hero-panel"></div>
  <svg class="hero-edge" width="1200" height="425" viewBox="0 0 1200 425">
    <line x1="794" y1="72" x2="599" y2="425" stroke="#c8202b" stroke-width="2"/>
    <line x1="780" y1="72" x2="585" y2="425" stroke="rgba(255,255,255,.15)" stroke-width="1"/>
  </svg>

  <nav class="nav">
    <div class="brand"><span class="sq"></span><span>Tallgrove Vale<br>Management</span></div>
    <ul class="menu">
      <li style="left:288px">Home</li>
      <li style="left:353px" class="active">About Us</li>
      <li style="left:441px">Services ⌄</li>
      <li style="left:539px">Owners</li>
      <li style="left:618px">Tenants</li>
      <li style="left:700px">Resources</li>
      <li style="left:795px">Contact Us</li>
    </ul>
    <div class="phone-box">
      <svg width="18" height="18" viewBox="0 0 24 24" fill="none" stroke="#fff" stroke-width="2"><path d="M5 3h4l2 5-2.5 1.5a11 11 0 0 0 6 6L16 13l5 2v4a2 2 0 0 1-2 2A17 17 0 0 1 3 5a2 2 0 0 1 2-2z"/></svg>
      (555) 204-7310
    </div>
  </nav>

  <h1 class="hero-title">About Us</h1>
  <div class="hero-rule"></div>
  <p class="hero-sub">Built on relationships.<br>Driven by expertise.<br>Focused on results.</p>
  <div class="hero-name">Tallgrove Vale<br>Management</div>
</header>

<section class="who">
  <div class="who-copy">
    <div class="eyebrow">WHO WE ARE</div>
    <h2 class="h2">Experience. Integrity.<br>Performance<span class="dot">.</span></h2>
    <p>At Tallgrove Vale Management, we specialize in managing properties in communities that others often overlook. Our team has built a strong reputation for successfully managing properties in high-concentration Section 8 markets by developing the relationships, systems, and expertise required to do it right.</p>
    <p>We are more than a management company—we are a strategic partner committed to protecting your investment and maximizing long-term value.</p>
    <a class="btn-red">Learn More About Our Services <span>›</span></a>
  </div>
  <div class="office" role="img" aria-label="Company conference room with a long table, chairs and city view windows"></div>
</section>

<section class="values">
  <div class="values-head">
    <div class="eyebrow">OUR VALUES</div>
    <h2 class="h2">The Principles That Guide Us</h2>
    <div class="bar"></div>
  </div>

  <div class="value" style="left:96px">
    <svg width="50" height="54" viewBox="0 0 50 54" fill="none" stroke-width="2.2"><path d="M25 3 45 10v16c0 13-9 21-20 25C14 47 5 39 5 26V10z" stroke="#1b2a57"/><circle cx="25" cy="27" r="8" stroke="#c8202b"/><path d="M25 27l8-8" stroke="#c8202b"/></svg>
    <h3>Integrity</h3>
    <p>We operate with honesty and transparency in every interaction.</p>
  </div>
  <div class="vdiv" style="left:288px"></div>
  <div class="value" style="left:298px">
    <svg width="56" height="54" viewBox="0 0 56 54" fill="none" stroke-width="2.2"><circle cx="28" cy="16" r="9" stroke="#1b2a57"/><path d="M12 50c0-11 7-18 16-18s16 7 16 18" stroke="#1b2a57"/><circle cx="10" cy="22" r="5" stroke="#c8202b"/><circle cx="46" cy="22" r="5" stroke="#c8202b"/></svg>
    <h3>Expertise</h3>
    <p>Decades of combined experience in managing complex properties.</p>
  </div>
  <div class="vdiv" style="left:489px"></div>
  <div class="value" style="left:498px">
    <svg width="54" height="54" viewBox="0 0 54 54" fill="none" stroke-width="2.2"><circle cx="25" cy="29" r="21" stroke="#1b2a57"/><circle cx="25" cy="29" r="13" stroke="#1b2a57"/><circle cx="25" cy="29" r="5" stroke="#c8202b"/><path d="M25 29 47 7M41 7h6v6" stroke="#c8202b"/></svg>
    <h3>Accountability</h3>
    <p>We take ownership and deliver on our promises every time.</p>
  </div>
  <div class="vdiv" style="left:690px"></div>
  <div class="value" style="left:700px">
    <svg width="66" height="50" viewBox="0 0 66 50" fill="none" stroke-width="2.2"><path d="M3 14l12-8 10 6M63 14l-12-8-14 8-8 8 4 4 10-6" stroke="#1b2a57"/><path d="M15 20l16 18c2 2 5 2 7 0l14-14M24 32l6 6M19 26l6 6" stroke="#c8202b"/></svg>
    <h3>Relationships</h3>
    <p>Strong partnerships with owners, tenants, and housing authorities.</p>
  </div>
  <div class="vdiv" style="left:893px"></div>
  <div class="value" style="left:904px">
    <svg width="56" height="54" viewBox="0 0 56 54" fill="none" stroke-width="2.2"><path d="M6 50h46" stroke="#1b2a57"/><path d="M10 50V36h8v14M24 50V28h8v14M38 50V20h8v30" stroke="#1b2a57"/><path d="M8 28 22 16l8 6 20-18M43 4h7v7" stroke="#c8202b"/></svg>
    <h3>Results</h3>
    <p>Focused on performance that drives long-term value.</p>
  </div>
</section>

<section class="team">
  <div class="team-copy">
    <div class="eyebrow">OUR TEAM</div>
    <h2 class="h2">A Team You Can Count On</h2>
    <p>Our team brings decades of hands-on experience in property management, leasing, compliance, and maintenance. We combine local knowledge with proven processes to deliver exceptional results for owners and residents.</p>
    <a class="btn-outline">Meet Our Team <span style="color:var(--red)">›</span></a>
  </div>
  <svg class="team-photo" width="1200" height="320" viewBox="0 0 1200 320">
    <defs>
      <linearGradient id="teamTone" x1="0" y1="0" x2="1" y2="0">
        <stop offset="0" stop-color="#9aa3b0"/><stop offset=".5" stop-color="#5e6674"/><stop offset="1" stop-color="#3a4254"/>
      </linearGradient>
    </defs>
    <polygon points="634,22 1165,22 1072,307 534,307" fill="url(#teamTone)" role="img" aria-label="Portrait of the management team standing together in an office"/>
    <polygon points="1160,0 1200,0 1200,20 1096,320 1086,320" fill="var(--navy)"/>
    <line x1="1200" y1="60" x2="1090" y2="320" stroke="#c8202b" stroke-width="3"/>
  </svg>
</section>

<section class="stats">
  <div class="stat" style="left:90px">
    <svg width="40" height="40" viewBox="0 0 40 40" fill="none" stroke="#fff" stroke-width="1.8"><path d="M4 38h32M8 38V4h14v34M22 14h10v24M12 9h2M16 9h2M12 15h2M16 15h2M12 21h2M16 21h2M12 27h2M16 27h2M26 20h2M26 26h2"/></svg>
    <div class="bar"></div><strong>500+</strong><span>Properties Managed</span>
  </div>
  <div class="sdiv" style="left:333px"></div>
  <div class="stat" style="left:343px">
    <svg width="46" height="40" viewBox="0 0 46 40" fill="none" stroke="#fff" stroke-width="1.8"><circle cx="23" cy="12" r="7"/><path d="M10 36c0-9 6-14 13-14s13 5 13 14"/><circle cx="9" cy="16" r="4" stroke="#c8202b"/><circle cx="37" cy="16" r="4" stroke="#c8202b"/></svg>
    <div class="bar"></div><strong>5,000+</strong><span>Units Under Management</span>
  </div>
  <div class="sdiv" style="left:597px"></div>
  <div class="stat" style="left:596px">
    <svg width="40" height="40" viewBox="0 0 40 40" fill="none" stroke="#fff" stroke-width="1.8"><rect x="4" y="7" width="32" height="30" rx="3"/><path d="M4 15h32M12 3v8M28 3v8"/><path d="M11 22h3M19 22h3M27 22h3M11 29h3M19 29h3" stroke="#c8202b"/></svg>
    <div class="bar"></div><strong>20+</strong><span>Years of Experience</span>
  </div>
  <div class="sdiv" style="left:829px"></div>
  <div class="stat" style="left:846px">
    <svg width="50" height="40" viewBox="0 0 50 40" fill="none" stroke="#fff" stroke-width="1.8"><path d="M2 12l9-6 8 5M48 12l-9-6-11 6-6 6 3 3 8-5"/><path d="M11 17l12 13c2 2 4 2 6 0l10-10" stroke="#c8202b"/></svg>
    <div class="bar"></div><strong>100%</strong><span>Commitment to Our Clients</span>
  </div>
</section>

<section class="cta" role="img" aria-label="Faded street of homes behind a call to action">
  <div class="cta-bar"></div>
  <h2>Let's Maximize Your Investment</h2>
  <p>Partner with a management team that understands your market, protects your assets, and drives results.</p>
  <a class="btn-red">Get Started Today <span>›</span></a>
</section>

<footer class="footer">
  <div class="f-brand"><span class="sq"></span><span>Tallgrove Vale<br>Management</span></div>
  <p class="f-blurb">Specializing in property management solutions for communities others won't—delivering results that matter.</p>
  <div class="f-social"><i></i><i></i><i></i></div>

  <div class="f-col" style="left:393px">
    <h4>Quick Links</h4>
    <ul><li>Home</li><li>About Us</li><li>Services</li><li>Owners</li><li>Tenants</li><li>Resources</li><li>Contact Us</li></ul>
  </div>
  <div class="f-col" style="left:610px">
    <h4>Services</h4>
    <ul><li>Property Management</li><li>Leasing Services</li><li>HAP Contract Management</li><li>Inspection Coordination</li><li>Maintenance Management</li><li>Financial Reporting</li></ul>
  </div>
  <div class="f-col f-contact" style="left:850px">
    <h4>Contact Us</h4>
    <ul>
      <li><svg width="16" height="16" viewBox="0 0 24 24" fill="none" stroke="#fff" stroke-width="2"><path d="M12 22s7-7 7-13a7 7 0 0 0-14 0c0 6 7 13 7 13z"/><circle cx="12" cy="9" r="2.5"/></svg><span>4820 Harmon Ridge Blvd, Suite 300<br>Fairhaven, OH 44190</span></li>
      <li><svg width="16" height="16" viewBox="0 0 24 24" fill="none" stroke="#fff" stroke-width="2"><path d="M5 3h4l2 5-2.5 1.5a11 11 0 0 0 6 6L16 13l5 2v4a2 2 0 0 1-2 2A17 17 0 0 1 3 5a2 2 0 0 1 2-2z"/></svg><span>(555) 204-7310</span></li>
      <li><svg width="16" height="16" viewBox="0 0 24 24" fill="none" stroke="#fff" stroke-width="2"><rect x="3" y="5" width="18" height="14" rx="2"/><path d="M3 7l9 6 9-6"/></svg><span>info@tallgrovevalemanagement.com</span></li>
      <li><svg width="16" height="16" viewBox="0 0 24 24" fill="none" stroke="#fff" stroke-width="2"><circle cx="12" cy="12" r="9"/><path d="M12 7v5l3 2"/></svg><span>Mon - Fri: 9:00 AM - 5:00 PM</span></li>
    </ul>
  </div>

  <div class="f-bottom"></div>
  <div class="f-copy">© 2025 Tallgrove Vale Management. All Rights Reserved.</div>
  <div class="f-legal"><span>Privacy Policy</span><span>|</span><span>Terms of Service</span></div>
</footer>

</body>
</html>
```